Business Card Design Project

We need a business card design for a immigration & education centre , we majoy help student with their visa and migration to australia . this is our home page . www.quorelpath.com.au
we prefer use the designer named Danu Weskatra the design with the QR code [Linked to Design #518099] is the way we want it done .
for further information please contact me
thanks
Reason: since the office is closed for holidays , i havent check my email often , so extend the dearline for a week ~
Hurry up great designers , the project will be end at end of this week .
looking forward to see you wonderful design !!!
Industry/Entity Type
Education
Look and feel
Each slider illustrates characteristics of the customer's brand and the style your logo design should communicate.

```html
<!DOCTYPE html>
<html lang="en">
<head>
<meta charset="utf-8">
<title>Quorelpath Business Card</title>
<link href="https://fonts.googleapis.com/css2?family=Exo:wght@600&family=Tinos&display=swap" rel="stylesheet">
<style>
  :root {
    --page: #ffffff;
    --card: #5588c4;
    --ink: #000000;
    --brand: #7fd0e6;
    --mark: #6cc04a;
    --divider: #3aa8d4;
    --divider-glow: #9fd6ee;
  }
  html, body {
    margin: 0;
    padding: 0;
    width: 1067px;
    height: 1200px;
    overflow: hidden;
    background: var(--page);
  }
  .sheet {
    position: relative;
    width: 1067px;
    height: 1200px;
  }
  .card {
    position: absolute;
    width: 945px;
    height: 534px;
    background: var(--card);
  }
  .card--front { left: 54px; top: 37px; }
  .card--back { left: 57px; top: 609px; }

  .brand-dot {
    position: absolute;
    border-radius: 50%;
    background: var(--mark);
  }
  .brand-name {
    position: absolute;
    margin: 0;
    font-family: "Exo", sans-serif;
    font-weight: 600;
    color: var(--brand);
    white-space: nowrap;
    transform: translateX(-50%);
  }

  .card--front .brand-dot { left: 423px; top: 70px; width: 100px; height: 100px; }
  .card--front .brand-name { left: 473px; top: 298px; font-size: 60px; line-height: 1; }

  .tagline {
    position: absolute;
    left: 0;
    right: 0;
    top: 384px;
    margin: 0;
    text-align: center;
    font-family: "Exo", sans-serif;
    font-weight: 600;
    font-size: 32px;
    line-height: 39px;
    color: var(--ink);
  }

  .card--back .brand-dot { left: 205px; top: 170px; width: 86px; height: 86px; }
  .card--back .brand-name { left: 248px; top: 292px; font-size: 48px; line-height: 1; }

  .divider {
    position: absolute;
    left: 478px;
    top: 61px;
    width: 6px;
    height: 400px;
    border-radius: 3px;
    background: var(--divider);
    box-shadow: 0 0 0 1px var(--divider-glow);
  }

  .contact {
    position: absolute;
    left: 552px;
    top: 85px;
    margin: 0;
    font-family: "Tinos", "Times New Roman", serif;
    font-size: 21.5px;
    line-height: 29px;
    color: var(--ink);
    font-style: normal;
  }
  .contact p { margin: 0 0 29px; }
  .contact p:last-child { margin-bottom: 0; }
</style>
</head>
<body>
<main class="sheet">
  <section class="card card--front">
    <span class="brand-dot" aria-hidden="true"></span>
    <h1 class="brand-name">Quorelpath</h1>
    <p class="tagline">Immigration &amp; Education Center<br>Your Path to Australia!<br>www.quorelpath.com.au</p>
  </section>

  <section class="card card--back">
    <span class="brand-dot" aria-hidden="true"></span>
    <p class="brand-name">Quorelpath</p>
    <div class="divider" aria-hidden="true"></div>
    <address class="contact">
      <p>Your Name Here<br>Position</p>
      <p>Address Here<br>xxxxxxxxxxxxxxxx<br>xxxxxxxxxxxx<br>xxxxxxxxx<br>xxxxx</p>
      <p>e-mail: youremail@example.com</p>
      <p>T.P : 04913527786</p>
    </address>
  </section>
</main>
</body>
</html>
```